Willowmere Paws Gala Sponsor & Stallholder Leaflet Design

Willowmere Paws Gala is the updated and refreshed version of the Brackenfield Pup Fair (See www.brackenfieldpupfair.co.uk).
Under new management, we need a leaflet designed to promote the event to potential stallholders and sponsors.
Willowmere Paws Gala is a fun day out for dogs and their human companions, with a range of activities for both.
As this is an outdoor event, we would like this theme in the leaflet.
It is being held in the grounds of Ashcombe Hall - http://www.ashcombehall.com
Attached is the required copy.
Note:
Leaflet format of DL/6 page is preferred, but will accept A5/4page
I will require the final work in InDesign format
Target Market(s)
Dog owners and lovers
Industry/Entity Type
Event
Look and feel

```html
<!DOCTYPE html>
<html lang="en">
<head>
<meta charset="utf-8">
<title>Trade Exhibitors – Stallholder Leaflet Panel</title>
<link rel="stylesheet" href="https://fonts.googleapis.com/css2?family=Archivo+Narrow:wght@700&family=Arimo:wght@400&display=swap">
<style>
  :root {
    --panel-bg: #e6e78f;
    --panel-bg-light: #ecec9c;
    --ink: #1f2016;
    --sky: #d3d6a6;
    --tree-dark: #4b5634;
    --tree-mid: #6e7b47;
    --lawn: #85954f;
    --lawn-deep: #6b7c3c;
  }
  html, body {
    margin: 0;
    padding: 0;
    width: 1200px;
    height: 2400px;
    overflow: hidden;
    background: var(--panel-bg);
  }
  .leaflet-panel {
    position: relative;
    width: 1200px;
    height: 2400px;
    overflow: hidden;
    background: linear-gradient(180deg, var(--panel-bg-light) 0%, var(--panel-bg) 60%);
    color: var(--ink);
    font-family: "Arimo", Arial, sans-serif;
  }
  .parkland-scene {
    position: absolute;
    left: 0;
    right: 0;
    bottom: 0;
    height: 1000px;
    background:
      linear-gradient(180deg, var(--panel-bg) 0%, rgba(230,231,143,0.85) 18%, rgba(211,214,166,0.6) 32%, rgba(110,123,71,0.55) 48%, rgba(75,86,52,0.7) 62%, rgba(133,149,79,0.9) 74%, var(--lawn) 86%, var(--lawn-deep) 100%);
    z-index: 0;
  }
  .content {
    position: relative;
    z-index: 1;
    padding: 0 78px 0 86px;
  }
  .section { position: absolute; left: 86px; right: 78px; }
  .section-title {
    font-family: "Archivo Narrow", "Arial Narrow", sans-serif;
    font-weight: 700;
    font-size: 46px;
    line-height: 1;
    margin: 0 0 10px;
    letter-spacing: 0.3px;
  }
  p, ul { margin: 0; font-size: 30px; line-height: 37px; }
  .gap { margin-top: 37px; }
  ul { list-style: none; padding: 0; }
  ul li { padding-left: 30px; position: relative; }
  ul li::before { content: "•"; position: absolute; left: 0; }
</style>
</head>
<body>
<main class="leaflet-panel">
  <div class="parkland-scene" role="img" aria-label="Photograph of parkland: a stately lawn with a stone balustrade and mature trees"></div>
  <div class="content">
    <section class="section trade-exhibitors" style="top:138px">
      <h2 class="section-title">TRADE EXHIBITORS</h2>
      <p>There are several space options available to exhibitors, both covered and grass space only. Covering the two days of the event, exhibitors also get a line listing in the event show guide and website.</p>
    </section>

    <section class="section grass-space" style="top:360px">
      <h2 class="section-title">GRASS SPACE ONLY</h2>
      <p>3m(w) x 6m(d) £150<br>6m(w) x 10m(d) £250<br>9m(w) x 10m(d) £350<br>12m(w) x 10m(d) £450</p>
      <p class="gap">Marquee Space - £15 per square meter (minimum 6 square meters)</p>
      <p class="gap">Power (Marquee Only) - £30 per 13amp Socket<br>Table (6' x 2'6") - £10 each</p>
    </section>

    <section class="section notes" style="top:820px">
      <h2 class="section-title">NOTES:</h2>
      <ul>
        <li>All exhibitors must have valid and suitable public, product &amp; employee liability insurance</li>
        <li>All (human) food based exhibitors must have suitable food hygiene qualifications andcertification</li>
      </ul>
      <p class="gap">Additional Marketing Opportunities</p>
    </section>

    <section class="section show-guide" style="top:1124px">
      <h2 class="section-title">SHOW GUIDE</h2>
      <p>A minimum of 32 pages, the show guide not only contains useful features and stories, but also a full listing of all sponsors and exhibitors.</p>
    </section>

    <section class="section advertiser-rates" style="top:1404px">
      <h2 class="section-title">EXHIBITOR STANDARD ADVERTISER</h2>
      <p>Back cover £350 £700<br>Full page £250 £500<br>Half Page £135 £2700<br>Quarter Page £75 £150<br>Sixth Page £50 £100</p>
    </section>

    <section class="section promotional-voucher" style="top:1722px">
      <h2 class="section-title">PROMOTIONAL VOUCHER</h2>
      <p>The centre of the guide will contain a pull out voucher booklet, with 6 vouchers per page. Exhibitors offering a special promotion, price or service during the event can promote it via a voucher, which will not only highlight the offer, but also identify the location of their stand. This costs £50 per voucher</p>
      <p class="gap">Banners in Competition Rings - £10 per meter (60cm high) - design &amp; production not included</p>
    </section>
  </div>
</main>
</body>
</html>
```